依頼詳細
マジックショーはステージがあります。
ショーの時間以外はテーブルマジックを行います。
堅い感じより柔らかい感じです。
楽しい、笑いのイメージ感です。
お店の広さは25坪くらいです。
まだ完成していませんが店内の写真添付します。
サイズを選ぶところがありますが、小さいのからある程度の大きさまでは印刷すると思います。

写真でロゴは添付しますが、データは決定した方に送りますので、その時に差し替えお願いします。
なので、案の時は何のフォントでもいいので入れ込んでください。
よろしくお願いします。
記載項目
順不同

奇術亭宇都宮店
2021年
1月18日グランドオープン

栃木県宇都宮市松原町2-5
梅川ビル2A
地図付けてください
028-3○○-1925(後ほど修正)
18時30分〜
定休日無し(不定休)
チラシ持参で500円OFF

毎日開催
ステージショーあり!
瞬き厳禁
テーブルマジックあり!

料金システム
フリータイム ¥2500(ワンドリンク制)
90分飲み放題付き¥3500
税別

楽しく元気になるお店
日本最大のエンターテイメント集団『奇術亭』がついに、宇都宮にオープン!
目の前で行われるプロのマジックと、ステージショーは必見!

#貸し切り#飲み放題#マジックショー#出張マジック
ハッシュタグみないに何個か思いつくのを入れるのもありかとも思っています。

とりあえずこんな的な感じです。それ以外の文言も入れてもらって構いませんし、こちらにある文章を変更していただいても構いません!

フライヤーを見て行ってみたいと思わせてくれるようなデザインに出会いたいです。

年末年始のタイミングでどれだけくるかわかりませんが、オープンが近いのでよろしくお願いします。
赤系、黄・オレンジ系、紫系
• 高解像度JPG (.jpg)
• イラストレーター形式 (.ai)
• フォトショップ形式 (.psd)
• PNG形式 (.png)
緊急事態宣言により、オープン日がズレました。
今後もどうなるかわからないので、日付を入れずにただのフライヤーで作成願います。
※今後も日付を入れる予定はないという事です。
■ 選んだ理由

スタッフでの多数決で決めさせて頂きました。

■ 提案者全員のお礼・コメント

たくさんのご応募ありがとうございました!

```html
<!DOCTYPE html>
<html lang="ja">
<head>
<meta charset="utf-8">
<title>奇術亭 宇都宮店 フライヤー</title>
<link rel="stylesheet" href="https://fonts.googleapis.com/css2?family=Dela+Gothic+One&family=Noto+Sans+JP:wght@500;700;900&display=swap">
<style>
  :root {
    --red: #e60012;
    --deep-red: #b0000c;
    --yellow: #ffe600;
    --ink: #1a1a1a;
    --paper: #ffffff;
    --band: #2a2a2a;
    --grey: #8a8a8a;
  }
  * { margin: 0; padding: 0; box-sizing: border-box; }
  html, body { width: 845px; height: 1200px; overflow: hidden; background: var(--paper); }
  .flyer {
    position: relative; width: 845px; height: 1200px; overflow: hidden;
    background: radial-gradient(circle at 50% 60%, #ffffff 0%, #f4f4f4 100%);
    font-family: "Noto Sans JP", sans-serif; color: var(--ink);
  }
  .header { position: absolute; top: 0; left: 0; width: 845px; height: 64px; background: var(--paper); }
  .brand {
    position: absolute; left: 34px; top: 8px;
    font-family: "Noto Sans JP", sans-serif; font-weight: 900; font-size: 40px; letter-spacing: 2px;
    color: var(--ink);
  }
  .stage-photo {
    position: absolute; top: 64px; left: 0; width: 845px; height: 400px;
    background:
      radial-gradient(ellipse at 58% 55%, #ff6a6a 0%, #d8142a 22%, #5a0610 55%, #1c0206 100%);
  }
  .coupon {
    position: absolute; left: 560px; top: 215px; width: 250px; height: 140px;
    background: var(--red); border: 4px solid var(--paper); border-radius: 18px;
    transform: rotate(-8deg); text-align: center; color: var(--paper);
    box-shadow: 0 4px 10px rgba(0,0,0,.35);
    padding-top: 18px;
  }
  .coupon-lead { font-weight: 900; font-size: 30px; line-height: 1.1; }
  .coupon-price { font-family: "Dela Gothic One", sans-serif; font-size: 44px; color: var(--yellow); line-height: 1.3; }
  .headline {
    position: absolute; left: 0; width: 845px; top: 468px; text-align: center;
    font-family: "Dela Gothic One", sans-serif; font-size: 76px; color: var(--red);
    letter-spacing: 2px; transform: skewX(-8deg);
    text-shadow: 3px 3px 0 #fff, -3px -3px 0 #fff, 3px -3px 0 #fff, -3px 3px 0 #fff, 5px 6px 0 rgba(0,0,0,.25);
  }
  .intro { position: absolute; left: 62px; top: 566px; width: 740px; font-weight: 700; font-size: 19px; line-height: 1.55; }
  .features { position: absolute; left: 40px; top: 660px; width: 765px; display: flex; justify-content: space-between; }
  .feature { width: 240px; text-align: center; }
  .feature-icon { width: 82px; height: 82px; margin: 0 auto 8px; border-radius: 50%; }
  .icon-curtain { background: linear-gradient(180deg, #d91f2c, #7d0a14); }
  .icon-cards { background: linear-gradient(180deg, #f0e5f4, #8a5aa8); }
  .icon-yen { background: var(--red); color: var(--paper); font-weight: 900; font-size: 46px; line-height: 82px; }
  .feature-title { font-weight: 900; font-size: 22px; }
  .feature-note { font-weight: 700; font-size: 18px; }
  .price-list { font-weight: 700; font-size: 15px; line-height: 1.35; }
  .price-list .accent { color: var(--red); }
  .map { position: absolute; left: 34px; top: 810px; width: 210px; height: 165px;
    background: linear-gradient(135deg, #eef0f2, #d6dade); border: 1px solid #c8c8c8; }
  .shop { position: absolute; left: 276px; top: 820px; width: 540px; }
  .shop-name { font-family: "Dela Gothic One", sans-serif; font-size: 62px; line-height: 1.1; }
  .shop-name .branch { font-size: 42px; margin-left: 10px; }
  .shop-rule { height: 3px; background: var(--ink); margin: 12px 0 10px; }
  .tags { font-weight: 700; font-size: 20px; color: var(--ink); }
  .footer {
    position: absolute; left: 0; bottom: 0; width: 845px; height: 58px; background: var(--band);
    color: var(--paper); font-weight: 500; font-size: 16px; line-height: 58px; text-align: center;
  }
</style>
</head>
<body>
<main class="flyer">
  <header class="header">
    <div class="brand">奇術亭</div>
  </header>

  <div class="stage-photo" role="img" aria-label="赤い照明に照らされた店内ステージの写真"></div>

  <div class="coupon">
    <div class="coupon-lead">チラシ持参で</div>
    <div class="coupon-price">500円OFF!</div>
  </div>

  <h1 class="headline">グランドオープン</h1>

  <p class="intro">
    楽しく元気になるお店☆<br>
    日本最大のエンターテイメント集団『奇術亭』がついに、宇都宮にオープン!<br>
    目の前で行われるプロのマジックと、ステージショーは必見!
  </p>

  <section class="features">
    <div class="feature">
      <div class="feature-icon icon-curtain" role="img" aria-label="ステージの幕のアイコン"></div>
      <div class="feature-title">毎日開催</div>
      <div class="feature-note">ステージショーあり!</div>
    </div>
    <div class="feature">
      <div class="feature-icon icon-cards" role="img" aria-label="トランプのアイコン"></div>
      <div class="feature-title">瞬き厳禁</div>
      <div class="feature-note">テーブルマジックあり!</div>
    </div>
    <div class="feature">
      <div class="feature-icon icon-yen">¥</div>
      <div class="feature-title">料金システム</div>
      <div class="price-list">
        フリータイム<br>
        <span class="accent">¥2500</span>(ワンドリンク制)<br>
        90分飲み放題付き<br>
        <span class="accent">¥3500</span>税別
      </div>
    </div>
  </section>

  <div class="map" role="img" aria-label="宇都宮店周辺の地図"></div>

  <section class="shop">
    <div class="shop-name">奇術亭<span class="branch">宇都宮店</span></div>
    <div class="shop-rule"></div>
    <div class="tags">#貸し切り#飲み放題#マジックショー#出張マジック</div>
  </section>

  <footer class="footer">
    栃木県宇都宮市松原町2-5 梅川ビル2A ・ 028-3○○-1925 ・ 18時30分〜 ・ 定休日無し（不定休）
  </footer>
</main>
</body>
</html>
```